need a marketing postcard to mail or drop off door-to-door. two categories of services, computer repairs, mobile device repairs. want an easily editable area/box for offering a discount

for more info, website is www.kelvaroshop.com

***Here is a link to an example postcard i like. Don't just copy it, it's there to give you an idea of what appeals to me.

http://shortlinko.net/qpw4tzd

Target Market(s)

Residential computer amd mobile device users/owners

Industry/Entity Type

Marketing

Requirements
Must have
• call out services provided in 2 sections: 1) computer services, 2)mobile device repair.

area easily editable to add discount such as "25% off with this card"

```html
<!DOCTYPE html>
<html lang="en">
<head>
<meta charset="utf-8">
<title>Kelvaro Tech Services – Postcard</title>
<link rel="stylesheet" href="https://fonts.googleapis.com/css2?family=Fredoka:wght@600&family=Oswald:wght@700&family=Open+Sans:wght@400;600;700&display=swap">
<style>
  :root{
    --page:#ffffff;
    --card:#ffffff;
    --card-fade:#e9ebee;
    --blue:#1b8fd6;
    --blue-dark:#1565b0;
    --green:#2e9a3e;
    --red:#c43a4c;
    --coupon:#b73848;
    --ink:#1a1a1a;
    --muted:#333a40;
    --photo-skin:#b9a192;
    --photo-grey:#9aa3ab;
    --photo-teal:#5b8f98;
    --photo-dark:#2b2f33;
  }
  *{box-sizing:border-box;margin:0;padding:0}
  html,body{width:904px;height:1200px;overflow:hidden;background:var(--page)}
  body{position:relative;font-family:"Open Sans",Arial,sans-serif;color:var(--ink)}

  .postcard{
    position:absolute;left:27px;width:853px;overflow:hidden;
    background:linear-gradient(180deg,var(--card) 55%,var(--card-fade) 100%);
    box-shadow:0 2px 8px rgba(0,0,0,.28);
  }
  .postcard--front{top:22px;height:557px}
  .postcard--back{top:614px;height:554px}
  .postcard > *{position:absolute}

  .swoosh{left:0;top:0}
  .photo{border-radius:2px}

  /* front */
  .photo--hero{left:28px;top:0;width:500px;height:222px;
    background:linear-gradient(120deg,var(--photo-grey),var(--photo-skin) 55%,#d9d2cc);
    border-bottom-right-radius:70% 100%;border-bottom-left-radius:30% 20%}
  .photo--technicians{left:344px;top:120px;width:150px;height:150px;border-radius:50%;
    background:radial-gradient(circle at 40% 40%,#e8e4e0,var(--photo-grey));
    border:8px solid var(--green)}
  .headline{left:504px;top:44px;width:340px;text-align:center;font-family:"Fredoka",Arial,sans-serif}
  .headline__lead{font-size:27px;line-height:1.2;color:var(--blue)}
  .headline__lead .and{color:var(--green)}
  .headline__main{font-size:40px;line-height:1.1;color:var(--red);letter-spacing:1px}

  .coupon{width:137px;height:189px;background:var(--coupon);padding:7px}
  .coupon__inner{width:100%;height:100%;border:2px dashed rgba(255,255,255,.8);
    color:#fff;text-align:center;padding-top:16px}
  .coupon__amount{font-family:"Oswald",Arial,sans-serif;font-size:60px;line-height:.95;display:block}
  .coupon__note{font-weight:700;font-size:14px;display:block;margin-top:14px}
  .front .coupon{left:549px;top:181px}
  .cut-line{height:2px;background:var(--coupon)}

  .photo--staff{width:138px;height:193px;
    background:linear-gradient(180deg,#f0e6d2 0%,#d9b98a 30%,var(--photo-teal) 60%,#4d7c84 100%)}
  .photo--icon{width:115px;height:85px;background:linear-gradient(160deg,#eef0f2,#b9c0c6)}
  .photo--diagnosis{left:335px;top:298px;width:225px;height:125px;
    background:linear-gradient(150deg,#e9ecef 10%,var(--blue-dark) 45%,var(--photo-dark) 90%)}

  .service__label{background:var(--blue);color:#fff;font-size:13px;text-align:center;
    border-radius:4px;padding:3px 6px;line-height:1.3}
  .service__text{font-size:10.5px;line-height:1.3;text-align:center;color:var(--muted)}

  .phone{font-weight:600;letter-spacing:.3px;color:var(--ink);line-height:1;white-space:nowrap}
  .address{font-weight:700;color:var(--green);white-space:nowrap}
  .web{font-weight:700;color:var(--blue-dark);white-space:nowrap}
  .divider{width:1px;background:#c9cdd1}

  .brand{display:flex;align-items:center;gap:10px}
  .brand__dot{width:50px;height:50px;border-radius:50%;background:var(--red);flex:none}
  .brand__name{font-weight:700;color:var(--ink);font-size:19px;line-height:1.1;white-space:nowrap}
  .experience{color:var(--red);font-size:20px;white-space:nowrap}

  /* back */
  .services-list{left:55px;top:14px;list-style:none}
  .services-list li{font-size:15px;line-height:22.3px;color:var(--blue)}
  .services-list li::before{content:"»";color:var(--green);margin-right:10px}
  .photo--handset{left:480px;top:10px;width:373px;height:204px;
    background:linear-gradient(150deg,var(--photo-dark) 20%,#5d6064 55%,var(--photo-skin) 85%);
    border-bottom-left-radius:60% 40%}
  .photo--devices{left:46px;top:232px;width:228px;height:140px;
    background:linear-gradient(120deg,#2a2d31,#7e8a95 50%,#dfe6ec)}
</style>
</head>
<body>

<section class="postcard postcard--front front">
  <div class="photo photo--hero" role="img" aria-label="Close-up of a technician holding a computer processor chip"></div>
  <svg class="swoosh" width="853" height="557" viewBox="0 0 853 557" aria-hidden="true">
    <path d="M10,0 C0,150 120,245 330,228 C520,212 650,150 853,200" fill="none" stroke="#c43a4c" stroke-width="16"/>
    <path d="M0,60 C30,200 150,262 340,246 C540,230 660,160 853,215" fill="none" stroke="#2e9a3e" stroke-width="10"/>
    <path d="M520,0 C470,80 560,150 853,170" fill="none" stroke="#1b8fd6" stroke-width="12"/>
    <path d="M540,0 C500,70 580,135 853,150" fill="none" stroke="#f2b632" stroke-width="4"/>
  </svg>
  <div class="photo photo--technicians" role="img" aria-label="Two technicians repairing a desktop computer"></div>

  <div class="headline">
    <p class="headline__lead">Computer <span class="and">and</span> Mobile</p>
    <p class="headline__main">PROBLEMS?!?</p>
  </div>

  <div class="photo photo--icon" style="left:40px;top:213px" role="img" aria-label="Laptop with a stethoscope"></div>
  <div class="photo photo--icon" style="left:196px;top:213px" role="img" aria-label="Tablet with a stethoscope"></div>

  <p class="service__label" style="left:36px;top:306px;width:140px">Computer Repair</p>
  <p class="service__text" style="left:36px;top:338px;width:140px">One of our core services and we have been reviving computers of all brands for over 25 years</p>
  <p class="service__label" style="left:188px;top:303px;width:130px">Mobile Device<br>Repair</p>
  <p class="service__text" style="left:184px;top:345px;width:138px">From cracked screens, to issues caused by software updates, the urge to hurl the device can be great! Resist that urge and bring your tablet or smartphone to us</p>

  <div class="photo photo--diagnosis" role="img" aria-label="Doctor reaching out of a laptop screen with a stethoscope"></div>

  <div class="coupon">
    <div class="coupon__inner">
      <span class="coupon__amount">25%<br>OFF</span>
      <span class="coupon__note">with this card</span>
    </div>
  </div>
  <div class="photo photo--staff" style="left:690px;top:177px" role="img" aria-label="Smiling customer service representative"></div>
  <div class="cut-line" style="left:549px;top:372px;width:290px"></div>
  <div class="divider" style="left:540px;top:374px;height:170px"></div>

  <p class="phone" style="left:66px;top:440px;font-size:50px">(555) 314 - 7260</p>
  <p class="address" style="left:70px;top:498px;font-size:14.5px">1820 Harbor Point Rd, Suite 5, Bayline FL 33990</p>
  <p class="web" style="left:150px;top:522px;font-size:19px">www.kelvaroshop.com</p>

  <div class="brand" style="left:596px;top:418px">
    <span class="brand__dot"></span>
    <span class="brand__name">Kelvaro<br>Tech Services</span>
  </div>
  <p class="experience" style="left:584px;top:522px">20+ years of experience</p>
</section>

<section class="postcard postcard--back">
  <ul class="services-list">
    <li>Virus &amp; Malware Removal</li>
    <li>System Optimization</li>
    <li>Training</li>
    <li>Business IT Services</li>
    <li>Computer Setup</li>
    <li>Data Recovery</li>
    <li>Network Services</li>
    <li>Cloud Backup</li>
    <li>Home Theatre</li>
  </ul>

  <svg class="swoosh" width="853" height="554" viewBox="0 0 853 554" aria-hidden="true">
    <path d="M300,0 C420,30 470,90 520,160 C560,215 640,240 730,225" fill="none" stroke="#c43a4c" stroke-width="10"/>
    <path d="M330,0 C470,20 560,40 853,60" fill="none" stroke="#2e9a3e" stroke-width="14"/>
    <path d="M420,0 C560,5 700,10 853,25" fill="none" stroke="#1b8fd6" stroke-width="10"/>
  </svg>
  <div class="photo photo--handset" role="img" aria-label="Hand inserting a SIM card into an opened smartphone"></div>

  <div class="coupon" style="left:284px;top:128px">
    <div class="coupon__inner">
      <span class="coupon__amount">25%<br>OFF</span>
      <span class="coupon__note">with this card</span>
    </div>
  </div>
  <div class="photo photo--staff" style="left:437px;top:150px;width:140px;height:173px" role="img" aria-label="Smiling customer service representative"></div>
  <div class="cut-line" style="left:284px;top:322px;width:412px"></div>

  <div class="photo photo--devices" role="img" aria-label="Desktop monitor, tablet, phone and laptop showing an error message"></div>

  <p class="phone" style="left:44px;top:390px;font-size:37px">(555) 314 - 7260</p>
  <p class="address" style="left:46px;top:436px;font-size:11.5px">1820 Harbor Point Rd, Suite 5, Bayline FL 33990</p>
  <p class="web" style="left:72px;top:454px;font-size:19px">www.kelvaroshop.com</p>

  <div class="brand" style="left:380px;top:366px">
    <span class="brand__dot"></span>
    <span class="brand__name">Kelvaro<br>Tech Services</span>
  </div>
  <p class="experience" style="left:358px;top:456px;font-size:19px">20+ years of experience</p>
</section>

</body>
</html>
```